Halvern Construction - Brochure

We need a graphic design for a company based in Vancouver, BC, Canada called 'Halvern Construction Ltd'. Halvern Construction is a company that specializes in building custom residential houses. The company has been in business for approximately 20 years. We specialize in building 1, 2, and 3 story houses as well as Laneway (coach) homes. We allow our customers to build there dream homes by working with our architects to build a design of there choosing. They also have all the options of choosing whatever materials they want in there houses for eg. doors, faucets, bathroom fixtures etc.We would like to see designs that use the color red and white.
Our second division of Halvern Construction is called "Halvern Environmental" which specializes in the testing and removal of hazardous materials i.e asbestos. The testing and removal of asbestos is a municipal requirement throughout the lower mainland. All hazardous materials must be removed prior to the demolition of any residential building. It would be nice to have parts of the brochure use the colour green to emphazise this companies colour.
Aside from other things, the brochure must mention:
- "Direct to builder, no real estate agent, No 3rd party commission"
- "We also specialize in Laneway Homes"
- "Customize your house the way you want! Come on in for a free consultation"
Also, the contact information:
- Office Address: 2837 Marlowe Street, Vancouver, BC V6R 1K9
- Email: info@halvernbuilds.example
- Phone: 604-555-0176
- Fax: 604-555-0177
- Website: www.halvernbuilds.example
We've re-read our task description and it says "We need a graphic design...". Actually what we meant to say is we are looking for someone who can create us a BROCHURE/FLYER, which can include graphic designs as we do not have one at the moment. We're looking for someone who can create a brochure that encompasses the information already provided and more. More information can be provided and probably will be provided once some designs have come our way. Sorry for the confusion!
We also want to include the following on the brochure:
We can BUY your old house for the purposes of resale or build a new house
We can TRADE your old house for one of our newly built houses
Target Market(s)
ages between 30-60 years old. People who can afford to build a home,

```html
<!DOCTYPE html>
<html lang="en">
<head>
<meta charset="utf-8">
<title>Halvern Construction – Brochure</title>
<link rel="stylesheet" href="https://fonts.googleapis.com/css2?family=Cinzel:wght@700&family=Archivo+Black&family=Arimo:wght@400;700&display=swap">
<style>
  :root {
    --backdrop: #e9e7e3;
    --slate: #4b4e57;
    --slate-dark: #3a3c43;
    --gold: #f0c02a;
    --red: #b3121d;
    --red-deep: #7d0a12;
    --red-bright: #d61f2a;
    --steel: #9a9ea6;
    --paper: #ffffff;
    --ink: #111111;
    --wood: #9a6a3c;
    --wood-dark: #7a4e27;
    --grey-shade: #d9d9dc;
    --eco-green: #3f8f2a;
    --eco-green-light: #b6e39a;
  }
  * { box-sizing: border-box; margin: 0; padding: 0; }
  html, body { width: 1200px; height: 900px; overflow: hidden; }
  body { background: var(--backdrop); font-family: "Arimo", Arial, sans-serif; position: relative; }

  .page { position: absolute; top: 180px; width: 360px; height: 540px; background: var(--paper); overflow: hidden; box-shadow: 0 4px 18px rgba(0,0,0,.18); }

  /* Cover */
  .cover { left: 40px; }
  .cover__masthead { position: absolute; inset: 0 0 auto 0; height: 92px; background: linear-gradient(180deg, var(--slate) 0%, var(--slate-dark) 100%); }
  .cover__company { position: absolute; top: 34px; left: 48px; font-family: "Cinzel", Georgia, serif; font-weight: 700; font-size: 14px; color: var(--gold); letter-spacing: .3px; }
  .cover__rule { position: absolute; top: 80px; left: 40px; right: 0; height: 3px; background: var(--gold); }
  .cover__photo { position: absolute; top: 92px; left: 0; right: 0; height: 110px; background: linear-gradient(180deg, #5f9ad6 0%, #b9d4ee 45%, #c99a6a 70%, #8c5a35 100%); }
  .cover__band { position: absolute; top: 202px; left: 0; right: 0; height: 10px; background: var(--steel); }
  .cover__panel { position: absolute; top: 212px; left: 0; right: 0; bottom: 0; background: radial-gradient(ellipse at 40% 30%, var(--red-bright) 0%, var(--red) 45%, var(--red-deep) 100%); }
  .cover__house-icon { position: absolute; top: 122px; right: 30px; width: 56px; height: 56px; border-radius: 6px; background: linear-gradient(160deg, #f4f4f4 0%, #c9c9c9 100%); }
  .cover__points { position: absolute; top: 380px; left: 24px; list-style: none; }
  .cover__points li { font-family: "Archivo Black", Arial, sans-serif; font-size: 19px; color: #b8bcc2; line-height: 30px; text-shadow: 1px 2px 0 #55585e; }
  .cover__points li::before { content: "- "; }

  /* Spread */
  .spread-left { left: 440px; box-shadow: 0 4px 18px rgba(0,0,0,.18), inset -14px 0 18px -14px rgba(0,0,0,.25); }
  .spread-right { left: 800px; box-shadow: 0 4px 18px rgba(0,0,0,.18), inset 14px 0 18px -14px rgba(0,0,0,.25); }

  .spread-left__wood { position: absolute; top: 0; left: 0; width: 96px; height: 100%; background: linear-gradient(90deg, var(--wood-dark), var(--wood) 50%, var(--wood-dark)); }
  .spread-left__art { position: absolute; inset: 0; }
  .spread-left__banner { position: absolute; top: 44px; left: 0; width: 300px; height: 76px; background: var(--slate); }
  .spread-left__title { position: absolute; top: 64px; left: 14px; font-family: "Arimo", Arial, sans-serif; font-weight: 700; font-size: 30px; color: var(--paper); letter-spacing: -.5px; }
  .spread-left__lead { position: absolute; top: 134px; left: 112px; width: 225px; font-weight: 700; font-size: 14.5px; line-height: 17px; color: var(--ink); }
  .spread-left__copy { margin-top: 6px; font-weight: 400; font-size: 8px; line-height: 10px; }
  .spread-left__photo { position: absolute; top: 330px; left: 0; width: 172px; height: 210px; background: linear-gradient(180deg, #7fb3e4 0%, #cfe3f2 50%, #7fa556 72%, #4d7a2e 100%); }

  .spread-right__photo { position: absolute; top: 0; left: 0; right: 0; height: 232px; background: linear-gradient(180deg, #dfe6e4 0%, #9bbd74 35%, #5b8f34 70%, #3f6c22 100%); }
  .spread-right__panel { position: absolute; top: 232px; left: 12px; right: 12px; height: 262px; padding: 16px 14px; background: linear-gradient(90deg, var(--red-deep) 0%, var(--red) 50%, var(--red-deep) 100%); color: var(--paper); }
  .spread-right__intro { font-weight: 700; font-size: 11.5px; line-height: 14px; }
  .spread-right__history { margin-top: 4px; font-weight: 700; font-size: 7.5px; line-height: 9.5px; }
  .spread-right__columns { margin-top: 16px; display: grid; grid-template-columns: 1fr 1fr; gap: 14px; font-size: 6px; line-height: 8px; }
  .spread-right__eco { color: var(--eco-green-light); }
  .spread-right__footer { position: absolute; top: 502px; left: 12px; right: 12px; font-size: 6px; line-height: 8px; color: var(--ink); }
  .spread-right__footer-label { font-weight: 700; color: var(--eco-green); }
</style>
</head>
<body>

<section class="page cover">
  <div class="cover__masthead"></div>
  <p class="cover__company">HALVERN CONSTRUCTION LTD.</p>
  <div class="cover__rule"></div>
  <div class="cover__photo" role="img" aria-label="Photo of two modern family houses under a blue sky"></div>
  <div class="cover__band"></div>
  <div class="cover__panel">
    <div class="cover__house-icon" role="img" aria-label="Small 3D house illustration with a red roof"></div>
  </div>
  <ul class="cover__points">
    <li>Comission Free</li>
    <li>Laneway Homes Specialist</li>
    <li>Full Customization</li>
  </ul>
</section>

<section class="page spread-left">
  <div class="spread-left__wood" role="img" aria-label="Wooden plank texture strip"></div>
  <svg class="spread-left__art" width="360" height="540" viewBox="0 0 360 540" aria-hidden="true">
    <polygon points="172,330 360,300 360,470 172,520" fill="var(--grey-shade)"/>
    <polygon points="172,400 300,380 270,470 172,490" fill="var(--red)"/>
    <polygon points="172,510 300,500 172,540" fill="var(--red)"/>
  </svg>
  <div class="spread-left__banner"></div>
  <h2 class="spread-left__title">CUSTOMISATION</h2>
  <div class="spread-left__lead">
    <p>Direct to builder, no real estate agent, no 3rd party commission.</p>
    <p class="spread-left__copy">Customize your house the way you want! Come on in for a free consultation. Work with our architects on a design of your choosing, then pick every material: doors, faucets, bathroom fixtures and more. We also specialize in Laneway Homes.</p>
  </div>
  <div class="spread-left__photo" role="img" aria-label="Photo of a man in a meadow sketching the frame of a house against the sky"></div>
</section>

<section class="page spread-right">
  <div class="spread-right__photo" role="img" aria-label="Photo of a green lawn with white line drawings of houses across it"></div>
  <div class="spread-right__panel">
    <p class="spread-right__intro">We are an experienced and dynamic construction firm which consists of a team of professionals. We provide the skills and equipment to plan, and deliver all kinds of residential buildings, regardless of size, and complexity we complete projects on time and within budget, making your dreams a reality.</p>
    <p class="spread-right__history">Our company has specialized in constructing new houses in traditional style, and modern style. With more than 10 years in the business of development and construction, Northshore Ridge Development, and Halvern Construction have been successfully developing and operating affordable housing for citizens.</p>
    <div class="spread-right__columns">
      <p>We can BUY your old house for the purposes of resale or build a new house. We can TRADE your old house for one of our newly built houses. We build 1, 2 and 3 story homes as well as Laneway (coach) homes.</p>
      <p class="spread-right__eco">Halvern Environmental tests for and removes hazardous materials such as asbestos. Removal is a municipal requirement across the Lower Mainland and must be done before any residential building is demolished.</p>
    </div>
  </div>
  <p class="spread-right__footer"><span class="spread-right__footer-label">Halvern Construction Ltd</span> · 2837 Marlowe Street, Vancouver, BC V6R 1K9 · Phone 604-555-0176 · Fax 604-555-0177 · info@halvernbuilds.example · www.halvernbuilds.example</p>
</section>

</body>
</html>
```